I need a book cover for a 6x9 book. The front cover information (title and author) is below, and the back cover information will be given to the winning designer. I am wanting something vibrant and bright, and I am open to your creativity, but I do not want any pictures of people on the cover. Save room for the barcode on the back cover.
Title:
Psst! Then Where?
Open Doors, Warm Rooms: Ideas for Lively Evenings Ahead
Author:
Derrion Platt

```html
<!DOCTYPE html>
<html lang="en">
<head>
<meta charset="utf-8">
<title>Psst! Then Where? — Book Cover</title>
<link rel="stylesheet" href="https://fonts.googleapis.com/css2?family=Lobster+Two:ital,wght@1,700&family=Architects+Daughter&display=swap">
<style>
  :root {
    --stage-bg: #e6e6e7;
    --cover-paper: #f4f4f2;
    --cover-facet: #dcdde2;
    --ink: #2b2b2b;
    --dot-yellow: #f2e21c;
    --dot-magenta: #d6246e;
    --lip-red: #c14a3c;
    --lip-deep: #8f2a22;
    --lip-inner: #c98a8a;
  }
  * { box-sizing: border-box; margin: 0; padding: 0; }
  html, body {
    width: 1200px;
    height: 900px;
    overflow: hidden;
    background: var(--stage-bg);
  }
  .stage {
    position: relative;
    width: 1200px;
    height: 900px;
  }
  .cover {
    position: absolute;
    left: 327px;
    top: 40px;
    width: 547px;
    height: 820px;
    background: var(--cover-paper);
    overflow: hidden;
    box-shadow: 0 10px 30px rgba(0,0,0,0.12);
  }
  .cover__facets {
    position: absolute;
    inset: 0;
    width: 100%;
    height: 100%;
  }
  .dot-band {
    position: absolute;
    background: linear-gradient(135deg, var(--dot-yellow) 0%, #f6ea6a 55%, #f3d8a0 100%);
    opacity: 0.85;
  }
  .dot-band--top { left: 250px; top: 0; width: 297px; height: 150px; }
  .dot-band--mid { left: 30px; top: 520px; width: 270px; height: 70px; }
  .dot-band--bottom { left: 0; top: 655px; width: 547px; height: 165px; }
  .cover__author {
    position: absolute;
    left: 82px;
    top: 78px;
    font-family: "Architects Daughter", sans-serif;
    font-size: 15px;
    color: var(--ink);
    letter-spacing: 0.3px;
  }
  .cover__title {
    position: absolute;
    left: 96px;
    top: 160px;
    font-family: "Lobster Two", cursive;
    font-style: italic;
    font-weight: 700;
    font-size: 50px;
    line-height: 1.05;
    color: var(--ink);
    transform: rotate(-4deg);
    transform-origin: left top;
  }
  .cover__title-line { display: block; }
  .cover__title-line--second { padding-left: 12px; font-size: 44px; }
  .cover__artwork {
    position: absolute;
    left: 100px;
    top: 310px;
    width: 380px;
    height: 200px;
    border-radius: 40% 40% 50% 50% / 30% 30% 70% 70%;
    background: radial-gradient(ellipse at 50% 40%, var(--lip-inner) 0%, var(--lip-red) 45%, var(--lip-deep) 100%);
  }
  .cover__subtitle {
    position: absolute;
    left: 140px;
    top: 560px;
    width: 380px;
    font-family: "Architects Daughter", sans-serif;
    font-size: 18px;
    line-height: 1.3;
    color: var(--ink);
    text-align: right;
    transform: rotate(-4deg);
  }
</style>
</head>
<body>
<main class="stage">
  <section class="cover" aria-label="Book front cover">
    <svg class="cover__facets" viewBox="0 0 547 820" aria-hidden="true">
      <polygon points="0,210 210,150 547,170 547,420 400,470 470,560 0,600" fill="var(--cover-facet)"/>
      <polygon points="0,0 250,0 250,120 0,150" fill="var(--cover-paper)"/>
      <polygon points="60,250 330,200 380,440 120,470" fill="var(--cover-paper)"/>
    </svg>

    <div class="dot-band dot-band--top" role="img" aria-label="Yellow and magenta halftone dot pattern"></div>
    <div class="dot-band dot-band--mid" role="img" aria-label="Yellow and magenta halftone dot pattern"></div>
    <div class="dot-band dot-band--bottom" role="img" aria-label="Yellow and magenta halftone dot pattern"></div>

    <p class="cover__author">Derrion Platt</p>

    <h1 class="cover__title">
      <span class="cover__title-line">Psst!</span>
      <span class="cover__title-line cover__title-line--second">Then Where?</span>
    </h1>

    <div class="cover__artwork" role="img" aria-label="Photo cutout of glossy red lips, slightly parted"></div>

    <p class="cover__subtitle">Open Doors, Warm Rooms:<br>Ideas for Lively Evenings Ahead</p>
  </section>
</main>
</body>
</html>
```